Business Card design for Recruiter providing Recruitment Staff Augmentation services

I need a double sided business card. I have used Zek to print cards in the past and really like their quality. I have a logo but need to change the tagline that is part of the graphic.

The tagline currently reads and Connnecting people with careers - but it should be removed.

The back should look like a notecard for writing a to do list with the first to-do Augment Recruiting Staff

```html
<!DOCTYPE html>
<html lang="en">
<head>
<meta charset="utf-8">
<title>Talent Forge – Business Card</title>
<link href="https://fonts.googleapis.com/css2?family=Lato:wght@400;700;900&display=swap" rel="stylesheet">
<style>
  :root {
    --backdrop: #2b2b2d;
    --navy: #0e4566;
    --navy-deep: #0b3a57;
    --ember: #c8482a;
    --paper: #f7f7f7;
    --ink: #173a52;
    --rule: #5d7383;
    --white: #ffffff;
  }
  * { box-sizing: border-box; margin: 0; padding: 0; }
  html, body {
    width: 1200px; height: 997px; overflow: hidden;
    background: var(--backdrop);
    font-family: "Lato", sans-serif;
  }
  .card {
    position: absolute; left: 270px;
    width: 660px; height: 377px;
    border-radius: 22px; overflow: hidden;
    background: var(--paper);
  }

  /* ---------- back: to-do note ---------- */
  .card--back { top: 90px; }
  .back__band {
    position: absolute; left: 0; top: 0; width: 100%; height: 130px;
    background: var(--navy);
    border-bottom: 4px solid var(--ember);
    display: flex; align-items: center; justify-content: center; gap: 16px;
  }
  .brand { display: flex; align-items: center; gap: 14px; font-weight: 700; letter-spacing: 3px; text-transform: uppercase; }
  .brand__dot { width: 34px; height: 34px; border-radius: 50%; }
  .back__band .brand { color: var(--white); font-size: 40px; margin-top: -14px; }
  .back__band .brand__dot { background: var(--white); }
  .back__tab {
    position: absolute; left: 50%; top: 112px; transform: translateX(-50%);
    width: 200px; height: 34px; border-radius: 10px;
    background: var(--ember); color: var(--white);
    font-size: 17px; letter-spacing: 1px;
    display: flex; align-items: center; justify-content: center;
  }
  .todo {
    position: absolute; top: 178px; left: 50px; right: 50px;
    display: grid; grid-template-columns: 1fr 1fr; column-gap: 60px;
  }
  .todo__col { list-style: none; }
  .todo__item {
    display: flex; align-items: flex-end; gap: 6px;
    height: 36px; color: var(--ink); font-size: 15px; font-weight: 700;
  }
  .todo__line { flex: 1; border-bottom: 1.5px solid var(--rule); height: 1px; margin-bottom: 3px; }
  .todo__text { font-weight: 700; }

  /* ---------- front: contact ---------- */
  .card--front { top: 530px; }
  .front__panel {
    position: absolute; left: 0; top: 0; bottom: 0; width: 285px;
    background: var(--navy-deep);
    border-right: 5px solid var(--ember);
    padding: 52px 0 0 42px;
    color: var(--white);
  }
  .holder__name { font-size: 25px; font-weight: 900; }
  .holder__role { color: var(--ember); font-size: 13px; font-weight: 700; letter-spacing: 1px; text-transform: uppercase; margin-top: 2px; }
  .contact { position: absolute; left: 42px; bottom: 48px; list-style: none; }
  .contact__row { display: flex; align-items: center; gap: 14px; font-size: 16px; margin-top: 14px; letter-spacing: .5px; }
  .contact__icon {
    width: 22px; height: 22px; background: var(--ember); border-radius: 2px;
    display: flex; align-items: center; justify-content: center;
  }
  .front__face {
    position: absolute; left: 290px; right: 0; top: 0; bottom: 0;
    display: flex; flex-direction: column; align-items: center; justify-content: center;
  }
  .front__face .brand { color: var(--ink); font-size: 36px; }
  .front__face .brand__dot { background: var(--ember); width: 30px; height: 30px; }
  .front__url { color: var(--ember); font-weight: 700; font-size: 19px; letter-spacing: .5px; margin-top: 52px; }
</style>
</head>
<body>

<section class="card card--back" aria-label="Card back: to-do list">
  <header class="back__band">
    <div class="brand"><span class="brand__dot"></span>Talent Forge</div>
  </header>
  <div class="back__tab">To-Do List</div>
  <div class="todo">
    <ol class="todo__col">
      <li class="todo__item"><span class="todo__text">1. Augment Recruiting Staff</span><span class="todo__line"></span></li>
      <li class="todo__item">2.<span class="todo__line"></span></li>
      <li class="todo__item">3.<span class="todo__line"></span></li>
      <li class="todo__item">4.<span class="todo__line"></span></li>
      <li class="todo__item">5.<span class="todo__line"></span></li>
    </ol>
    <ol class="todo__col">
      <li class="todo__item">6.<span class="todo__line"></span></li>
      <li class="todo__item">7.<span class="todo__line"></span></li>
      <li class="todo__item">8.<span class="todo__line"></span></li>
      <li class="todo__item">9.<span class="todo__line"></span></li>
      <li class="todo__item">10.<span class="todo__line"></span></li>
    </ol>
  </div>
</section>

<section class="card card--front" aria-label="Card front: contact details">
  <div class="front__panel">
    <h1 class="holder__name">Moo Zek</h1>
    <p class="holder__role">Founder &amp; CEO</p>
    <ul class="contact">
      <li class="contact__row">
        <span class="contact__icon">
          <svg width="14" height="14" viewBox="0 0 24 24" fill="#fff"><path d="M6.6 10.8a15.1 15.1 0 0 0 6.6 6.6l2.2-2.2c.3-.3.7-.4 1-.2 1.1.4 2.3.6 3.6.6.6 0 1 .4 1 1V20c0 .6-.4 1-1 1A17 17 0 0 1 3 4c0-.6.4-1 1-1h3.5c.6 0 1 .4 1 1 0 1.3.2 2.5.6 3.6.1.3 0 .7-.2 1l-2.3 2.2z"/></svg>
        </span>555-014-2290
      </li>
      <li class="contact__row">
        <span class="contact__icon">
          <svg width="14" height="14" viewBox="0 0 24 24" fill="#fff"><path d="M3 5h18v14H3z" fill="none" stroke="#fff" stroke-width="2"/><path d="M3 5l9 8 9-8" fill="none" stroke="#fff" stroke-width="2"/></svg>
        </span>moo@talentforge.com
      </li>
    </ul>
  </div>
  <div class="front__face">
    <div class="brand"><span class="brand__dot"></span>Talent Forge</div>
    <p class="front__url">www.talentforge.com</p>
  </div>
</section>

</body>
</html>
```